Email Signature & Facebook Cover Design – Birchlane Study Centre

I’m looking for a clean, professional email signature and a matching Facebook cover photo for my tutoring business, Birchlane Study Centre.
The email signature needs to display properly across Outlook and iPhone without the image appearing as an attachment. It should include my logo and contact details and have a friendly but professional look suitable for an education business.
Details to include:
Moira Dunholt
Director & Lead Tutor
Birchlane Study Centre
hello@birchlanestudy.co.uk
www.birchlanestudy.co.uk
01632 418736
The Facebook cover should match the branding, feel professional and welcoming, and be optimised for desktop and mobile.

```html
<!DOCTYPE html>
<html lang="en">
<head>
<meta charset="utf-8">
<title>Birchlane Study Centre – Email Signature</title>
<link rel="stylesheet" href="https://fonts.googleapis.com/css2?family=Archivo:wght@700&family=Raleway:wght@400;500;600;700&display=swap">
<style>
  :root {
    --backdrop: #7a4a26;
    --card: #ffffff;
    --brand-green: #45bb6d;
    --ink: #2c2a2e;
    --on-green: #ffffff;
  }
  * { box-sizing: border-box; margin: 0; padding: 0; }
  html, body {
    width: 1200px;
    height: 1200px;
    overflow: hidden;
  }
  body {
    background: var(--backdrop);
    display: flex;
    align-items: center;
    justify-content: center;
    font-family: "Raleway", sans-serif;
  }
  .signature {
    position: relative;
    width: 1080px;
    height: 484px;
    background: var(--card);
  }
  .name-band {
    position: absolute;
    left: 41px;
    right: 41px;
    top: 55px;
    height: 108px;
    background: var(--brand-green);
    color: var(--on-green);
    display: flex;
    align-items: baseline;
    justify-content: center;
    padding-top: 20px;
    gap: 26px;
    white-space: nowrap;
  }
  .person-name {
    font-family: "Archivo", sans-serif;
    font-weight: 700;
    font-size: 60px;
    letter-spacing: -0.5px;
  }
  .person-role {
    font-weight: 500;
    font-size: 44px;
  }
  .brand-name {
    position: absolute;
    left: 60px;
    top: 222px;
    width: 270px;
    color: var(--brand-green);
    font-weight: 700;
    font-size: 52px;
    line-height: 1.08;
  }
  .contact-list {
    position: absolute;
    left: 526px;
    top: 212px;
    list-style: none;
  }
  .contact-item {
    display: flex;
    align-items: baseline;
    height: 80px;
  }
  .contact-label {
    width: 59px;
    color: var(--brand-green);
    font-weight: 400;
    font-size: 34px;
  }
  .contact-value {
    color: var(--ink);
    font-weight: 600;
    font-size: 31px;
  }
</style>
</head>
<body>
  <section class="signature">
    <header class="name-band">
      <span class="person-name">Moira Dunholt,</span>
      <span class="person-role">Director &amp; Lead Tutor</span>
    </header>

    <div class="brand-name">Birchlane<br>Study<br>Centre</div>

    <ul class="contact-list">
      <li class="contact-item"><span class="contact-label">M:</span><span class="contact-value">01632 418736</span></li>
      <li class="contact-item"><span class="contact-label">E:</span><span class="contact-value">hello@birchlanestudy.co.uk</span></li>
      <li class="contact-item"><span class="contact-label">W:</span><span class="contact-value">www.birchlanestudy.co.uk</span></li>
    </ul>
  </section>
</body>
</html>
```